Web Design Project

I need designs (PSD only - no programming) for several pages of a new website helping train operators to manage key information about their traindrivers.
The main feature of this website is the management of personnel records (create, edit, search, delete). Another key aspect is the management of user privileges. Since this is a new website we also need a user friendly frontpage, pricing information and how it works sections.
This can be broken down into 9 pages for which we need designs (PSDs).
1. Home
2. Driver record
3. How it works
4. Pricing
5. User administration
6. Help
7. Record list view
8. Login
9. Registration
Navigation (not logged in) are: Home | How it works | Pricing | Customers | About us | Contact
Navigation (logged in) are: Overview | Administration | Manage records | Billing | Help | Contact
Footer: Customer logos | Awards | Terms & Conditions | Privacy
To provide the best support for you to come up with a strong design proposal I will provide DAILY feedback to all participants. We have also created concept mockups (attached) and example pages (below) for each section to give you a clear sense of what we look for.
The core concepts for a successful bid are that the website is EASY to understand, INTUITIVE to navigate, and SIMPLE to use. Most of our users lack technical background and are looking for tool to simplify their work.
The strongest participants (winner and close contenders) will have the opportunity to additional commissioned work on additional sections not included in this brief.
Example Pages (by section)
1. http://www.quorvane.example/site-keepers/
1. http://www.vrm.example/
1. http://www.tovasko.example/
1. http://www.glimmerhootz.example/
2. http://www.pendlo.example/profile_edit.gne
3. https://www.drav.example/how-it-works/
3. http://www.wexalot.example/learn
4. http://www.brindlequay.example/crm/editions-pricing.jsp
4. http://www.quorvane.example/site-keepers/rates
6. https://support.zoltu.example/en-gb/
6. http://help.harbenquill.example/contact_us
8. https://www.morvelnet.example/uas/login
8. https://www.harbenquill.example/login
8. http://www.ublix.example/login/index
For form designs we like Ferrowen, Okvo, Pendlo, Morvelnet, Trellimap and the concepts presented by Dario Fenstermack in his classic Panel Craft Beyond the Checkboxes.
For additional guidance see mockups attached!
Target Market(s)
Security, human resources and admin support employees for train operators.
Industry/Entity Type
Learn
Requirements
Should not have
- Home page should not have
Social media icons (trellimap, pellomb, Morvelnet, RSS feed)
Contact forms
Read more links
Old trains

```html
<!DOCTYPE html>
<html lang="en">
<head>
<meta charset="utf-8">
<title>RailLedger – Home</title>
<link rel="stylesheet" href="https://fonts.googleapis.com/css2?family=Arimo:wght@400;700&family=Gelasio:wght@400;700&family=PT+Sans:wght@400;700&display=swap">
<style>
:root{
  --blue:#1a93e0;
  --blue-dark:#0b6fc1;
  --blue-light:#5cc2f5;
  --green:#7cc21a;
  --green-dark:#4f9a0b;
  --text:#222;
  --muted:#555;
  --rule:#d9d9d9;
  --link:#1a86d4;
  --white:#fff;
}
*{box-sizing:border-box;margin:0;padding:0}
html,body{width:1015px;height:1200px;overflow:hidden;background:var(--white)}
body{position:relative;font-family:"Arimo",Arial,sans-serif;color:var(--text)}
.abs{position:absolute}
.brand{left:140px;top:12px;font-family:"Gelasio",Georgia,serif;font-weight:700;font-size:37px;color:var(--blue)}
.top-links{right:143px;top:26px;display:flex;align-items:center;gap:10px;font-size:12px}
.top-links a{color:var(--link);text-decoration:none}
.top-links .sep{width:1px;height:13px;background:var(--rule)}
.lang{width:94px;height:19px;border:1px solid #bbb;font-size:10px;color:#999;padding:3px 5px;position:relative;background:var(--white)}
.lang::after{content:"";position:absolute;right:0;top:0;width:16px;height:17px;background:var(--green)}
.lang svg{position:absolute;right:4px;top:6px;z-index:1}
.hero{left:0;top:106px;width:1015px;height:249px;background:linear-gradient(180deg,var(--blue-light),var(--blue) 45%,var(--blue-dark))}
.hero-top{left:0;top:80px;width:1015px;height:26px;background:linear-gradient(180deg,#fff,#d6eefb)}
.nav{left:140px;top:72px;width:731px;height:35px;display:flex;background:linear-gradient(180deg,#9ad532,var(--green-dark));border-radius:3px 3px 0 0}
.nav a{flex:1;color:var(--white);font-size:13px;font-weight:700;text-decoration:none;display:flex;align-items:center;justify-content:center;border-left:1px solid rgba(255,255,255,.35)}
.nav a:first-child{border-left:0;background:linear-gradient(180deg,#55c0f4,var(--blue));border-radius:3px 0 0 0}
.hero-title{left:175px;top:138px;font-family:"PT Sans",Arial,sans-serif;font-weight:700;font-size:58px;line-height:49px;color:var(--white)}
.hero-title span{display:block;padding-left:20px}
.hero-sub{left:177px;top:243px;font-family:"PT Sans",Arial,sans-serif;font-size:19px;color:var(--white)}
.btn{display:flex;align-items:center;justify-content:center;color:var(--white);font-size:15px;background:linear-gradient(180deg,#8fd22a,var(--green-dark));border-radius:4px;box-shadow:0 1px 2px rgba(0,0,0,.3)}
.hero-btn{left:172px;top:281px;width:190px;height:30px}
.slide-frame{left:381px;top:131px;width:452px;height:182px;background:var(--white);padding:5px;box-shadow:0 2px 6px rgba(0,0,0,.3)}
.photo{width:100%;height:100%}
.photo-train{background:linear-gradient(180deg,#b7b0a6,#5a5147 55%,#d9d7d4)}
.arrow{top:178px}
.dots{left:454px;top:329px;display:flex;gap:10px}
.dots i{width:12px;height:12px;border-radius:50%;background:var(--white);display:block}
.dots i:first-child{background:var(--green)}
.section-title{left:140px;font-family:"Gelasio",Georgia,serif;font-size:23px;color:var(--blue)}
.section-title b{font-weight:700}
.rule{left:140px;width:731px;height:1px;background:var(--rule)}
.feature{width:220px;height:80px}
.feature .icon{position:absolute;left:0;top:0;width:78px;height:78px;border-radius:50%}
.feature h3{position:absolute;left:87px;top:0;font-size:15px;font-weight:400;color:var(--text)}
.feature p{position:absolute;left:87px;top:22px;width:133px;font-size:9.4px;line-height:10px;text-align:justify;color:var(--muted)}
.vdiv{width:1px;background:linear-gradient(180deg,transparent,#ddd 20%,#ddd 80%,transparent)}
.step{width:195px}
.step-head{display:flex;align-items:center;gap:10px;font-size:24px;color:#333;font-family:"Arimo",Arial,sans-serif}
.step-num{width:36px;height:36px;border-radius:50%;background:var(--blue);color:var(--white);font-weight:700;font-size:20px;display:flex;align-items:center;justify-content:center}
.step-pic{margin-top:14px;width:195px;height:112px;border:3px solid #e5e5e5}
.step h4{margin-top:10px;font-size:19px;font-weight:400}
.step p{margin-top:4px;font-size:9.3px;line-height:11px;color:var(--muted);text-align:justify}
.partners{left:140px;top:1070px;width:731px;display:flex;justify-content:space-between;align-items:center}
.partner{width:82px;height:56px;border-radius:8px;background:#d7d7d7}
.partner.round{border-radius:50%;width:56px}
.footer{left:0;top:1160px;width:1015px;height:40px;background:linear-gradient(180deg,var(--blue),var(--blue-dark));color:var(--white);font-size:9.5px}
.footer .legal{position:absolute;left:143px;top:17px}
.footer .fnav{position:absolute;right:143px;top:17px;display:flex;gap:6px}
.footer .fnav b{font-weight:700}
.back-top{left:962px;top:1088px}
</style>
</head>
<body>

<div class="abs hero-top"></div>
<div class="abs hero"></div>

<div class="abs brand">RailLedger</div>
<div class="abs top-links">
  <a href="#">Sign up</a><span class="sep"></span>
  <a href="#">Login</a><span class="sep"></span>
  <a href="#">Language</a>
  <div class="lang">English
    <svg width="8" height="5" viewBox="0 0 8 5"><path d="M0 0h8L4 5z" fill="#fff"/></svg>
  </div>
</div>

<nav class="abs nav">
  <a href="#">Home</a><a href="#">How it Works</a><a href="#">Prices</a><a href="#">Our Customers</a><a href="#">About us</a><a href="#">Contact</a>
</nav>

<svg class="abs arrow" style="left:138px" width="26" height="80" viewBox="0 0 26 80"><path d="M24 2 4 40l20 38V62L12 40 24 18z" fill="#2a2a2a" stroke="#fff" stroke-width="2"/></svg>
<svg class="abs arrow" style="left:850px" width="26" height="80" viewBox="0 0 26 80"><path d="M2 2l20 38L2 78V62l12-22L2 18z" fill="#2a2a2a" stroke="#fff" stroke-width="2"/></svg>

<h1 class="abs hero-title">Fresh<span>ideas</span></h1>
<div class="abs hero-sub">for the Varrow culture</div>
<a class="abs btn hero-btn" href="#">Sign up or Request a call</a>

<div class="abs slide-frame">
  <div class="photo photo-train" role="img" aria-label="Freight locomotive hauling cars through a snowy landscape"></div>
</div>
<div class="abs dots"><i></i><i></i><i></i><i></i><i></i></div>

<h2 class="abs section-title" style="top:372px"><b>Why will</b> you choose us?</h2>
<div class="abs rule" style="top:407px"></div>

<div class="abs feature" style="left:140px;top:423px">
  <div class="icon" style="background:radial-gradient(circle,#f6d35a,#c98a10)" role="img" aria-label="Gold satisfaction guarantee seal"></div>
  <h3>Satisfaction</h3>
  <p>Lorem Ipsum is simply dummy text of the printing and typesetting industry. Lorem Ipsum has specimenbook.been the indus</p>
</div>
<div class="abs vdiv" style="left:377px;top:418px;height:80px"></div>
<div class="abs feature" style="left:395px;top:423px">
  <div class="icon" style="border-radius:6px;background:linear-gradient(180deg,#f2f2f2,#8a8a8a)" role="img" aria-label="Businessman in a suit, human resources symbol"></div>
  <h3>Human Resources</h3>
  <p>Lorem Ipsum is simply dummy text of the printing and typesetting industry. Lorem Ipsum has specimenbook.been the indus</p>
</div>
<div class="abs vdiv" style="left:636px;top:418px;height:80px"></div>
<div class="abs feature" style="left:651px;top:423px">
  <div class="icon" style="border-radius:6px;background:linear-gradient(135deg,#f4f4f4,#b5b5b5)" role="img" aria-label="Bunch of silver keys"></div>
  <h3>Admin Support</h3>
  <p>Lorem Ipsum is simply dummy text of the printing and typesetting industry. Lorem Ipsum has specimenbook.been the indus</p>
</div>

<div class="abs feature" style="left:140px;top:520px">
  <div class="icon" style="background:radial-gradient(circle,#3aa6b8,#0d3d4c 70%,#c9c9c9 72%)" role="img" aria-label="Round radar screen, security symbol"></div>
  <h3>Security</h3>
  <p>Lorem Ipsum is simply dummy text of the printing and typesetting industry. Lorem Ipsum has specimenbook.been the indus</p>
</div>
<div class="abs vdiv" style="left:377px;top:515px;height:80px"></div>
<div class="abs feature" style="left:395px;top:520px">
  <div class="icon" style="background:radial-gradient(circle,#1e90d8,#0c3e73 55%,#6bbf2a 56%,#2f7c10)" role="img" aria-label="Blue and green circular sync arrows"></div>
  <h3>No IT Guys Needed</h3>
  <p>Lorem Ipsum is simply dummy text of the printing and typesetting industry. Lorem Ipsum has specimenbook.been the indus</p>
</div>
<div class="abs vdiv" style="left:636px;top:515px;height:80px"></div>
<div class="abs feature" style="left:651px;top:520px">
  <div class="icon" style="background:radial-gradient(circle,#e6cfa0,#8d6a3a)" role="img" aria-label="Bronze award medal"></div>
  <h3>Winning Award</h3>
  <p>Lorem Ipsum is simply dummy text of the printing and typesetting industry. Lorem Ipsum has specimenbook.been the indus</p>
</div>

<a class="abs btn" href="#" style="left:392px;top:623px;width:228px;height:29px">Sign up or Request a call</a>

<h2 class="abs section-title" style="top:672px"><b>How</b> it works?</h2>
<div class="abs rule" style="top:712px"></div>

<div class="abs vdiv" style="left:372px;top:728px;height:272px"></div>
<div class="abs vdiv" style="left:640px;top:728px;height:272px"></div>

<div class="abs step" style="left:140px;top:732px">
  <div class="step-head">STEP <span class="step-num">1</span></div>
  <div class="step-pic" role="img" aria-label="Blue and yellow locomotives seen from above in a depot" style="background:linear-gradient(180deg,#4a6fa8,#2c3f6a 60%,#8a5a3a)"></div>
  <h4>Lorem Ipsum</h4>
  <p>Lorem Ipsum is simply dummy text of the printing and typesetting industry. Lorem Ipsum has been the industry's standard dummy text ever since the 1500s, when an unknown printer took a galley of type and scrambled it to make a type specimen book.</p>
</div>
<div class="abs step" style="left:408px;top:732px">
  <div class="step-head">STEP <span class="step-num">2</span></div>
  <div class="step-pic" role="img" aria-label="Train driver in a safety vest inside the cab" style="background:linear-gradient(135deg,#9aa7ad,#4d5a58 55%,#c8d040)"></div>
  <h4>Lorem Ipsum</h4>
  <p>Lorem Ipsum is simply dummy text of the printing and typesetting industry. Lorem Ipsum has been the industry's standard dummy text ever since the 1500s, when an unknown printer took a galley of type and scrambled it to make a type specimen book.</p>
</div>
<div class="abs step" style="left:676px;top:732px">
  <div class="step-head">STEP <span class="step-num">3</span></div>
  <div class="step-pic" role="img" aria-label="Freight train curving through autumn trees" style="background:linear-gradient(160deg,#c44a1a,#7a3a1c 50%,#4b4a3a)"></div>
  <h4>Lorem Ipsum</h4>
  <p>Lorem Ipsum is simply dummy text of the printing and typesetting industry. Lorem Ipsum has been the industry's standard dummy text ever since the 1500s, when an unknown printer took a galley of type and scrambled it to make a type specimen book.</p>
</div>

<h2 class="abs section-title" style="top:1017px"><b>Our</b> Partners</h2>
<div class="abs rule" style="top:1058px"></div>
<div class="abs partners">
  <div class="partner" role="img" aria-label="Partner badge"></div>
  <div class="partner round" role="img" aria-label="Partner badge"></div>
  <div class="partner" role="img" aria-label="Partner badge"></div>
  <div class="partner round" role="img" aria-label="Partner badge"></div>
  <div class="partner" style="width:110px" role="img" aria-label="Partner badge"></div>
</div>

<footer class="abs footer">
  <div class="legal">Copyright © RailLedger 2012. All right reserved. &nbsp; | &nbsp;Terms &amp; Conditions</div>
  <div class="fnav"><b>Home</b> · <span>How it Works</span> · <span>Prices</span> · <span>Our Customers</span> · <span>About us</span> · <span>Contact</span></div>
</footer>

<svg class="abs back-top" width="28" height="107" viewBox="0 0 28 107" aria-label="Back to top">
  <path d="M0 10 14 0l14 10v97l-14-10L0 107z" fill="#2b2b2b"/>
  <text x="18" y="90" transform="rotate(-90 18 90)" fill="#fff" font-family="Arimo, Arial, sans-serif" font-size="9" font-weight="700">BACK TO TOP</text>
</svg>

</body>
</html>
```